Letterbox promotional card

Boutique real estate agency needs postcard (no address/stamp space) to promote business via letterboxing, café distribution, etc.
Needs contact details as per attached business card, clean look, company colours, logo and catch phrase as per the T-shirt design attached.
Do not include 'Sales' from the business card. Add another name and mobile number-
Velko Marrandine 0438 917 264

Target Market(s)

Potential property vendors.

Industry/Entity Type

Real Estate

Requirements
Must have
• REVISEDText for reverse side of card: Use dot points, one per line - (no dot point for the Considering selling?)-
• Considering selling?
• No obligation appraisal
• Integrity
• Personalised service
• Individualised marketing programs
• Quality
Nice to have
• Considering selling?
• No obligation appraisal
• Integrity
• Personalised service
Should not have
• Property photos; too much text

```html
<!DOCTYPE html>
<html lang="en">
<head>
<meta charset="utf-8">
<title>Velko Marrandine Real Estate – Letterbox Card</title>
<link rel="stylesheet" href="https://fonts.googleapis.com/css2?family=PT+Sans:wght@400;700&display=swap">
<style>
  :root {
    --navy: #0d3544;
    --gold: #9a7d2a;
    --mist: #f1f1f1;
    --paper: #ffffff;
    --ink: #1f2a30;
    --backdrop: #e4e2de;
  }
  * { box-sizing: border-box; margin: 0; padding: 0; }
  html, body { width: 1200px; height: 1000px; overflow: hidden; }
  body {
    position: relative;
    background: var(--backdrop);
    font-family: "PT Sans", Arial, sans-serif;
    color: var(--ink);
  }
  .card {
    position: absolute;
    background: var(--paper);
    overflow: hidden;
    box-shadow: 0 4px 14px rgba(0,0,0,.25);
  }
  .band { position: absolute; left: 0; right: 0; }
  .band--navy { background: var(--navy); }
  .band--gold { background: var(--gold); }
  .band--mist { background: var(--mist); }
  .band-text {
    color: #fff; text-align: center; width: 100%;
    display: flex; align-items: center; justify-content: center; height: 100%;
  }
  .wordmark {
    position: absolute; color: var(--navy); font-weight: 700;
    text-transform: uppercase; text-align: center; line-height: 1.05;
  }

  /* Front */
  .card--front { left: 62px; top: 20px; width: 598px; height: 460px; }
  .card--front .band--navy { top: 0; height: 30px; }
  .card--front .band--mist { top: 268px; height: 157px; }
  .card--front .band--gold { bottom: 0; height: 35px; }
  .card--front .band-text { font-size: 25px; }
  .card--front .wordmark { left: 0; right: 0; top: 98px; font-size: 44px; letter-spacing: 1px; }
  .place { position: absolute; left: 0; right: 0; top: 290px; text-align: center; font-size: 29px; color: var(--navy); }
  .tagline { position: absolute; left: 0; right: 0; top: 334px; text-align: center; font-size: 35px; color: var(--gold); }

  /* Back */
  .card--back { left: 520px; top: 510px; width: 597px; height: 458px; }
  .card--back .band--navy { top: 0; height: 40px; }
  .card--back .band--navy .band-text { font-size: 25px; }
  .card--back .band--mist { top: 253px; height: 170px; }
  .card--back .band--gold { bottom: 0; height: 35px; }
  .card--back .band--gold .band-text { font-size: 12.5px; }
  .card--back .wordmark { left: 22px; width: 222px; top: 72px; font-size: 28px; }
  .divider { position: absolute; left: 272px; top: 75px; width: 3px; height: 312px; background: var(--gold); }
  .pitch { position: absolute; left: 305px; top: 70px; }
  .pitch h2 { font-size: 18px; font-weight: 700; color: var(--navy); margin-bottom: 6px; }
  .pitch ul { list-style: none; }
  .pitch li { font-size: 16px; line-height: 23px; display: flex; align-items: center; }
  .pitch li::before { content: ""; width: 9px; height: 9px; margin-right: 11px; background: var(--gold); }
  .pitch li:nth-child(even)::before { background: var(--navy); }
  .agent { position: absolute; top: 231px; width: 110px; text-align: center; font-size: 13px; }
  .agent .portrait {
    width: 87px; height: 113px; margin: 0 auto 10px;
    border: 4px solid var(--gold);
    background: linear-gradient(160deg, #b9b4a6, #7d7c70);
  }
  .agent .mobile { display: flex; align-items: center; justify-content: center; gap: 4px; margin-top: 2px; }
  .agent--one { left: 17px; }
  .agent--two { left: 138px; }
  .contact { position: absolute; left: 305px; top: 296px; list-style: none; }
  .contact li { display: flex; align-items: center; gap: 9px; font-size: 15.5px; line-height: 24.5px; }
  .contact svg { width: 13px; height: 13px; fill: var(--ink); }
</style>
</head>
<body>

<section class="card card--front">
  <div class="band band--navy"></div>
  <div class="wordmark">Velko<br>Marrandine<br>Real Estate</div>
  <div class="band band--mist"></div>
  <p class="place">Goulburn</p>
  <p class="tagline">Making a difference</p>
  <div class="band band--gold"><div class="band-text">www.marrandinerealty.com</div></div>
</section>

<section class="card card--back">
  <div class="band band--navy"><div class="band-text">www.marrandinerealty.com</div></div>
  <div class="band band--mist"></div>
  <div class="wordmark">Velko<br>Marrandine<br>Real Estate</div>

  <div class="agent agent--one">
    <div class="portrait" role="img" aria-label="Portrait photo of Maren Holloway"></div>
    <div>Maren Holloway</div>
    <div class="mobile"><svg width="8" height="12" viewBox="0 0 8 12"><rect x=".5" y=".5" width="7" height="11" rx="1" fill="none" stroke="#1f2a30"/><rect x="1.5" y="2" width="5" height="7" fill="#1f2a30"/></svg>0421 304 786</div>
  </div>
  <div class="agent agent--two">
    <div class="portrait" role="img" aria-label="Portrait photo of Velko Marrandine"></div>
    <div>Velko Marrandine</div>
    <div class="mobile"><svg width="8" height="12" viewBox="0 0 8 12"><rect x=".5" y=".5" width="7" height="11" rx="1" fill="none" stroke="#1f2a30"/><rect x="1.5" y="2" width="5" height="7" fill="#1f2a30"/></svg>0438 917 264</div>
  </div>

  <div class="divider"></div>

  <div class="pitch">
    <h2>Considering selling?</h2>
    <ul>
      <li>No obligation appraisal</li>
      <li>Integrity</li>
      <li>Personalised service</li>
      <li>Individualised marketing programs</li>
      <li>Quality</li>
    </ul>
  </div>

  <ul class="contact">
    <li><svg viewBox="0 0 12 12"><path d="M6 0a4 4 0 0 0-4 4c0 3 4 8 4 8s4-5 4-8a4 4 0 0 0-4-4zm0 5.5A1.5 1.5 0 1 1 6 2.5a1.5 1.5 0 0 1 0 3z"/></svg>214 Carrick St, Goulburn NSW 2580</li>
    <li><svg viewBox="0 0 12 12"><path d="M1 3c0-1 1-2 5-2s5 1 5 2v1H8V3H4v1H1zM3 5h6l2 6H1z"/></svg>02 4830 5147</li>
    <li><svg viewBox="0 0 12 12"><path d="M3 0h5v4H3zM1 4h10v8H1zm2 2v1h2V6zm4 0v1h2V6zM3 8v1h2V8zm4 0v1h2V8z"/></svg>02 4830 5192</li>
    <li><svg viewBox="0 0 12 12"><text x="0" y="10" font-size="12" font-family="PT Sans, sans-serif">@</text></svg>velko@marrandinerealty.com</li>
  </ul>

  <div class="band band--gold"><div class="band-text">Real Estate and Stock and Station Agent Licence Number 2096315 &nbsp;|&nbsp; ABN 41 608 253 917</div></div>
</section>

</body>
</html>
```